In Home Personal IT Consultant (Nerd) Website and Logo QTgeek.net

Website and logo design for in home personal "nerd". Consulting services provided: Home Automation, Home Theater, Network and Wi-Fi installation, Computer Repair, and Virus Removal. Need simple site to promote QTgeek.net based in Santa Fe, New Mexico. You may choose to incorporate the Zia symbol from the New Mexico flag into the design, not mandatory. I am also a big fan of the movie Return of the Tinkers.
I have over 10 years of experience in the hospitality industry working with multi million dollar hotels and will apply that same level of service to the home. TechVara B+ and Shieldwise+ Certified. Available by appointment, primarily Evenings and Weekends. Consulting rate will be $70/hr.
Industry/Entity Type
Consulting
Number of Pages Required
1 page
Look and feel
Each slider illustrates characteristics of the customer's brand and the style your logo design should communicate.

```html
<!DOCTYPE html>
<html lang="en">
<head>
<meta charset="utf-8">
<title>QTgeek.net – In Home IT Personal Consultant</title>
<link href="https://fonts.googleapis.com/css2?family=Open+Sans:wght@300;400;600;700&display=swap" rel="stylesheet">
<style>
:root{
  --red:#c10f3c;
  --red-dark:#9e0c31;
  --ink:#222;
  --text:#555;
  --muted:#777;
  --white:#fff;
  --light:#f1f1f1;
  --dark:#1c1c1c;
  --footer:#262626;
  --hero-a:#8a7566;
  --hero-b:#3c3430;
}
*{box-sizing:border-box;margin:0;padding:0}
html,body{width:1200px;height:3543px;overflow:hidden}
body{font-family:"Open Sans",Arial,sans-serif;color:var(--text);background:var(--white);position:relative}
.abs{position:absolute}
section,header,footer{position:absolute;left:0;width:1200px}

/* header */
.site-header{top:0;height:165px;background:var(--white)}
.brand{display:flex;align-items:center;gap:14px}
.brand-dot{width:42px;height:42px;border-radius:50%;background:var(--red)}
.brand-name{font-weight:700;font-size:34px;color:var(--ink);letter-spacing:.5px}
.site-header .brand{left:86px;top:58px}
.header-phone{left:558px;top:46px;font-size:22px;color:var(--ink);display:flex;align-items:center;gap:8px}
.social{display:flex;gap:8px}
.social span{width:22px;height:22px;background:var(--red);border-radius:3px;display:block}
.site-header .social{left:745px;top:48px}
.appointment{left:904px;top:43px;border:2px solid var(--red);color:var(--red);border-radius:20px;padding:4px 16px;font-size:15px}
.main-nav{left:450px;top:108px;display:flex;gap:0;width:662px;justify-content:space-between;font-size:17px;color:var(--ink)}

/* hero */
.hero{top:165px;height:563px;background:linear-gradient(160deg,var(--hero-a),var(--hero-b) 70%,#6e6259)}
.hero .text{width:1200px;text-align:center;color:var(--white);top:212px}
.hero h1{font-size:96px;font-weight:600;letter-spacing:2px;line-height:1}
.hero p{font-size:38px;margin-top:12px}
.slider-arrow{top:274px;width:26px;height:26px;border-radius:50%;background:rgba(0,0,0,.55)}

/* about */
.about{top:728px;height:559px}
.round-photo{border-radius:50%;border:3px solid var(--white);box-shadow:0 0 0 2px #999}
.about .round-photo{left:92px;top:829px;width:340px;height:340px;background:linear-gradient(140deg,#e9eef2,#9aa9b5)}
.about-head{left:520px;top:120px;display:flex;gap:14px;align-items:center}
.about-head .brand-dot{width:56px;height:56px}
.about h2{font-size:36px;font-weight:400;color:var(--ink);line-height:1}
.about h3{font-size:19px;font-weight:400;color:var(--ink);margin-top:4px}
.about .copy{left:520px;top:210px;width:640px;font-size:15px;line-height:1.62;text-align:justify}
.btn{background:var(--red);color:var(--white);border-radius:22px;font-size:16px;padding:10px 26px;display:inline-block}
.about .btn{left:512px;top:390px}

/* services */
.services{top:1287px;height:551px;background:linear-gradient(120deg,#2a2a2a,var(--dark) 60%,#111)}
.services h2{width:1200px;text-align:center;top:78px;color:var(--white);font-size:36px;font-weight:400}
.service{width:250px;text-align:center;color:var(--white);top:193px}
.service .icon{width:114px;height:114px;border-radius:50%;background:var(--red);margin:0 auto;display:flex;align-items:center;justify-content:center;border:3px solid #e34]}
.service h4{font-size:19px;font-weight:400;margin-top:36px}
.service p{font-size:13px;line-height:1.5;margin-top:8px}
.service .more{font-size:13px;margin-top:8px;display:block}

/* what we do */
.what{top:1838px;height:543px}
.what h2{left:128px;top:130px;font-size:37px;font-weight:600;color:var(--ink)}
.what .copy{left:128px;top:185px;width:558px;font-size:15px;line-height:1.68;text-align:justify}
.what .btn{left:130px;top:370px}
.what .round-photo{left:744px;top:92px;width:330px;height:330px;background:linear-gradient(180deg,#6b3a26,#b36a3f 60%,#5a3224)}

/* blog */
.blog{top:2381px;height:588px;background:var(--light)}
.blog h2{width:1200px;text-align:center;top:86px;font-size:36px;font-weight:400;color:var(--ink)}
.blog .lead{width:1200px;text-align:center;top:147px;font-size:14px;color:var(--ink)}
.post{top:203px;width:312px}
.post .thumb{height:173px}
.post .meta{display:flex;margin-top:16px;font-size:12px}
.post .meta .date{background:var(--red);color:var(--white);padding:3px 12px}
.post .meta .count{background:#333;color:var(--white);padding:3px 10px}
.post h4{font-size:17px;font-weight:400;color:var(--ink);margin-top:14px}
.post p{font-size:13px;line-height:1.5;margin-top:8px;color:var(--muted)}
.post .more{font-size:13px;color:var(--red);margin-top:8px;display:block}

/* certifications */
.certs{top:2969px;height:236px}
.cert{top:59px;height:123px;border:2px solid #ccc;background:var(--white);padding:12px}
.cert span{display:block;width:100%;height:100%;background:linear-gradient(180deg,var(--red) 0 55%,#e8e8e8 55%)}

/* footer */
.site-footer{top:3205px;height:338px;background:var(--footer);color:#ddd}
.site-footer .brand{left:86px;top:122px}
.site-footer .brand-name{color:var(--white);font-size:30px}
.col{top:70px}
.col h5{font-size:15px;font-weight:400;color:var(--white);letter-spacing:.5px;margin-bottom:20px}
.contact-line{display:flex;gap:14px;font-size:13px;line-height:1.5;margin-bottom:14px}
.links li{list-style:none;font-size:13px;margin-bottom:8px}
.links li::before{content:"» ";color:#aaa}
.mail p{font-size:13px;line-height:1.5;width:200px}
.mail form{display:flex;margin-top:14px}
.mail .field{width:148px;height:30px;background:var(--white);color:#999;font-size:12px;padding:7px 10px}
.mail .submit{background:var(--red);color:var(--white);font-size:13px;padding:6px 12px}
.footer-rule{left:86px;top:262px;width:1028px;height:1px;background:#444}
.copyright{left:86px;top:289px;font-size:12px}
.site-footer .social{left:976px;top:286px}
.site-footer .social span{background:#ddd}
</style>
</head>
<body>

<header class="site-header">
  <div class="brand abs"><span class="brand-dot"></span><span class="brand-name">qtgeek</span></div>
  <div class="header-phone abs">
    <svg width="18" height="18" viewBox="0 0 24 24"><rect width="24" height="24" rx="4" fill="var(--red)"/><path d="M8 5l2 4-1.5 1.5a9 9 0 0 0 5 5L15 14l4 2-1 3c-7 0-13-6-13-13z" fill="#fff"/></svg>
    505/555-0148
  </div>
  <div class="social abs"><span></span><span></span><span></span><span></span></div>
  <div class="appointment abs">Available by Appointment</div>
  <nav class="main-nav abs">
    <span>HOME</span><span>ABOUT US</span><span>SERVICES</span><span>SUPPORT</span><span>BLOG</span><span>CONTACT</span>
  </nav>
</header>

<section class="hero" role="img" aria-label="Photo of hands repairing an open laptop with a tool">
  <span class="slider-arrow abs" style="left:70px"></span>
  <span class="slider-arrow abs" style="left:1104px"></span>
  <div class="text abs">
    <h1>QTGEEK</h1>
    <p>I'm an Inhome IT Personal Consultant</p>
  </div>
</section>

<div class="round-photo abs" style="left:92px;top:829px;width:340px;height:340px;background:linear-gradient(140deg,#e9eef2,#9aa9b5)" role="img" aria-label="Photo of a hand holding a smart home control tablet"></div>
<section class="about">
  <div class="about-head abs">
    <span class="brand-dot"></span>
    <div><h2>ABOUT US</h2><h3>Neque porro quisquam est qui dolorem</h3></div>
  </div>
  <p class="copy abs">It is a long established fact that a reader will be distracted by the readable content of a page when looking at its layout. The point of using Lorem Ipsum is that it has a more-or-less normal distribution of letters, as opposed to using 'Content here, content here', making it look like readable English. Many desktop publishing packages and web page editors now use Lorem Ipsum as their default model text, and a search for 'lorem ipsum' will uncover many web sites still in their infancy. Various versions have evolved over the years, sometimes by accident, sometimes on purpose</p>
  <span class="btn abs">Consulting rate will be $70/hr</span>
</section>

<section class="services" role="region" aria-label="Our services, over a dim photo of a technician at work">
  <h2 class="abs">OUR SERVICES</h2>
  <div class="service abs" style="left:64px">
    <div class="icon"><svg width="52" height="52" viewBox="0 0 48 48" fill="none" stroke="#fff" stroke-width="2.5"><path d="M8 22L24 9l16 13v17H8z"/><path d="M18 28a9 9 0 0 1 12 0M21 32a4 4 0 0 1 6 0"/></svg></div>
    <h4>Home Automation</h4>
    <p>It has survived not only five centuries, but also the leap into electronic</p>
    <span class="more">Read More -&gt;</span>
  </div>
  <div class="service abs" style="left:333px">
    <div class="icon"><svg width="52" height="52" viewBox="0 0 48 48" fill="none" stroke="#fff" stroke-width="2.5"><rect x="8" y="8" width="32" height="32" rx="3"/><circle cx="18" cy="20" r="5"/><circle cx="18" cy="32" r="3"/><path d="M28 16h7M28 22h7M28 28h7M28 34h7"/></svg></div>
    <h4>Home Theater</h4>
    <p>It has survived not only five centuries, but also the leap into electronic</p>
    <span class="more">Read More -&gt;</span>
  </div>
  <div class="service abs" style="left:593px">
    <div class="icon"><svg width="52" height="52" viewBox="0 0 48 48" fill="none" stroke="#fff" stroke-width="2.5"><rect x="10" y="11" width="28" height="20" rx="2"/><path d="M5 36h38M18 18l12 8"/></svg></div>
    <h4>Computer Repair</h4>
    <p>It has survived not only five centuries, but also the leap into electronic</p>
    <span class="more">Read More -&gt;</span>
  </div>
  <div class="service abs" style="left:860px">
    <div class="icon"><svg width="52" height="52" viewBox="0 0 48 48" fill="none" stroke="#fff" stroke-width="2.5"><path d="M12 14h24M20 14v-4h8v4M15 14l2 26h14l2-26M21 20v14M27 20v14"/></svg></div>
    <h4>Virus Removal</h4>
    <p>It has survived not only five centuries, but also the leap into electronic</p>
    <span class="more">Read More -&gt;</span>
  </div>
</section>

<section class="what">
  <h2 class="abs">WHAT WE DO?</h2>
  <p class="copy abs">We're moving from a generation of workers who grew up in a world where information was scarce and predominately controlled by a minority of society who traded it to generate significant wealth. Millennials on the other hand have only experienced a world with the internet. A world where information flowed freely. A world where there were little to no barriers of entry to creating a platform to disseminate knowledge. This difference in lived experiences has a material impact on behavior at an individual and aggregated company level.</p>
  <span class="btn abs">Primarily Evenings and Weekends</span>
  <div class="round-photo abs" role="img" aria-label="Photo of a home theater room with a wall mounted screen and speakers"></div>
</section>

<section class="blog">
  <h2 class="abs">LATEST BLOG</h2>
  <p class="lead abs">It has survived not only five centuries, but also the leap into electronic typesetting.</p>
  <article class="post abs" style="left:94px">
    <div class="thumb" role="img" aria-label="Photo of a modern living room with a television wall" style="background:linear-gradient(135deg,#d9d6d0,#5b5550)"></div>
    <div class="meta"><span class="date">Dec 03</span><span class="count">0</span></div>
    <h4>Neque porro quisquam dolorem</h4>
    <p>It has survived not only five centuries, but also the leap into electronic typesetting.</p>
    <span class="more">View More »</span>
  </article>
  <article class="post abs" style="left:444px">
    <div class="thumb" role="img" aria-label="Photo of hands soldering a circuit board" style="background:linear-gradient(135deg,#c9b79a,#6d6a73)"></div>
    <div class="meta"><span class="date">Dec 03</span><span class="count">0</span></div>
    <h4>Porro quisquam est qui</h4>
    <p>It has survived not only five centuries, but also the leap into electronic typesetting.</p>
    <span class="more">View More »</span>
  </article>
  <article class="post abs" style="left:798px">
    <div class="thumb" role="img" aria-label="Illustration of a monitor inspected with a magnifying glass" style="background:linear-gradient(180deg,#3fb6e6,#1d8fc7)"></div>
    <div class="meta"><span class="date">Dec 03</span><span class="count">0</span></div>
    <h4>Dolorem ipsum quia dolor</h4>
    <p>It has survived not only five centuries, but also the leap into electronic typesetting.</p>
    <span class="more">View More »</span>
  </article>
</section>

<section class="certs" aria-label="Certifications">
  <div class="cert abs" style="left:229px;width:246px"><span></span></div>
  <div class="cert abs" style="left:539px;width:139px"><span></span></div>
  <div class="cert abs" style="left:742px;width:226px"><span></span></div>
</section>

<footer class="site-footer">
  <div class="brand abs"><span class="brand-dot"></span><span class="brand-name">qtgeek</span></div>
  <div class="col abs" style="left:366px">
    <h5>CONTACT US</h5>
    <div class="contact-line"><svg width="14" height="18" viewBox="0 0 14 18"><path d="M7 0a7 7 0 0 0-7 7c0 5 7 11 7 11s7-6 7-11a7 7 0 0 0-7-7z" fill="#fff"/><circle cx="7" cy="7" r="2.5" fill="var(--footer)"/></svg><span>240 Canyon Road, Suite<br>12 Santa Fe, NM</span></div>
    <div class="contact-line"><svg width="14" height="14" viewBox="0 0 24 24"><path d="M6 2l4 6-3 3a13 13 0 0 0 6 6l3-3 6 4-2 4C10 22 2 14 2 4z" fill="#fff"/></svg><span>505.555.0192</span></div>
    <div class="contact-line"><svg width="14" height="12" viewBox="0 0 14 12"><rect width="14" height="12" fill="#fff"/><path d="M0 1l7 5 7-5" stroke="var(--footer)" fill="none" stroke-width="1.5"/></svg><span>hello@qtgeek.net</span></div>
  </div>
  <div class="col abs" style="left:687px">
    <h5>QUICK LINKS</h5>
    <ul class="links"><li>About us</li><li>My Services</li><li>Events</li><li>Blog</li></ul>
  </div>
  <div class="col mail abs" style="left:905px">
    <h5>JOIN OUR MAILING LIST</h5>
    <p>Your about us information would fit here nicely.</p>
    <form><span class="field">Email address</span><span class="submit">Submit</span></form>
  </div>
  <div class="footer-rule abs"></div>
  <p class="copyright abs">Copyright © 2017. All Rights Reserved</p>
  <div class="social abs"><span></span><span></span><span></span><span></span></div>
</footer>

</body>
</html>
```